Marlowe Fenwick Certifiers needs a flyer design!

We need a flyer designed to reach out to professionals such as architects and town planners that will tell them they should use us for commercial projects. Needs to be professional but capture they're attention.
We provide Grade 1 building certification and we are looking to do less residential smaller jobs and move into the larger commercial jobs to grow the company and move forward.
We would like the designs to use blue, black, white and grey.

Reason: Hello, I am hoping by extending the deadline we will receive a few more designs that have great impact, yet with the content needed to attract higher end clients to use our service. I would like the GRADE ONE CERTIFICATION element pushed in the flyer and specialist etc etc.. Happy designing and Thank you!

```html
<!DOCTYPE html>
<html lang="en">
<head>
<meta charset="utf-8">
<title>Marlowe Fenwick Certifiers – Flyer</title>
<link href="https://fonts.googleapis.com/css2?family=Open+Sans:wght@400;600;700;800&family=Great+Vibes&display=swap" rel="stylesheet">
<style>
  :root {
    --blue: #2f6fc2;
    --blue-dark: #1b4fa3;
    --blue-deep: #123c86;
    --ink: #222;
    --text: #5a5a5a;
    --grey: #8a8a8a;
    --grey-light: #e4e4e4;
    --white: #ffffff;
    --backdrop: #d9dadb;
    --orange: #e58a2a;
  }
  * { box-sizing: border-box; margin: 0; padding: 0; }
  html, body { width: 1200px; height: 800px; overflow: hidden; }
  body { background: var(--backdrop); font-family: "Open Sans", Arial, sans-serif; color: var(--text); }

  .flyer { position: absolute; left: 30px; top: 20px; width: 1140px; height: 760px; background: var(--white); overflow: hidden; box-shadow: 0 4px 18px rgba(0,0,0,.18); }

  .hero-photo { position: absolute; left: 0; top: 0; width: 100%; height: 200px;
    background: linear-gradient(160deg, #2a3646 0%, #3c4a52 40%, #46563f 75%, #2d3a2c 100%); }

  .surveyor-plate { position: absolute; left: 22px; top: 22px; width: 380px; height: 150px; background: rgba(255,255,255,.82); padding: 8px 18px; }
  .surveyor-name { font-family: "Great Vibes", cursive; font-size: 50px; color: #7a7a7a; line-height: 1.05; }
  .surveyor-title { font-size: 19px; color: var(--blue); font-weight: 600; line-height: 1.3; }

  .card { position: absolute; background: var(--white); border-radius: 6px; box-shadow: 0 3px 10px rgba(0,0,0,.22); padding: 12px; display: flex; gap: 12px; }
  .card-photo { flex: none; border-radius: 3px; }
  .card h3 { font-size: 14px; font-weight: 800; color: var(--blue); text-transform: uppercase; line-height: 1.15; margin-bottom: 4px; }
  .card p { font-size: 10.5px; font-weight: 600; color: var(--ink); line-height: 1.35; }

  .card-why { left: 22px; top: 210px; width: 380px; height: 150px; }
  .card-why .card-photo { width: 140px; height: 124px; background: linear-gradient(#c9d6e4, #e8e4dc); }
  .card-approval { left: 420px; top: 210px; width: 360px; height: 150px; }
  .card-approval .card-photo { width: 130px; height: 124px; background: linear-gradient(#b9b4ad, #8a8680); }
  .card-quote { left: 800px; top: 26px; width: 320px; height: 122px; align-items: center; }
  .card-quote .card-photo { width: 130px; height: 98px; background: linear-gradient(#a9b8a2, #7d8f86); }
  .card-quote h3 { font-size: 15px; }
  .quote-call { font-size: 14px; color: var(--grey); }
  .quote-phone { font-size: 19px; color: var(--orange); font-weight: 600; }

  .specialties { position: absolute; left: 800px; top: 170px; width: 320px; height: 330px; background: var(--white); box-shadow: 0 3px 10px rgba(0,0,0,.18); }
  .specialties h2 { background: var(--grey-light); color: var(--blue); font-size: 17px; font-weight: 700; text-transform: uppercase; padding: 10px 18px; }
  .specialties ul { list-style: none; padding: 10px 18px; }
  .specialties li { font-size: 12.5px; font-weight: 600; color: var(--ink); padding: 5px 0; display: flex; align-items: center; gap: 8px; }
  .specialties svg { flex: none; }

  .feature { position: absolute; }
  .feature h2 { font-size: 17px; font-weight: 800; color: var(--blue); text-transform: uppercase; line-height: 1.3; margin-bottom: 6px; }
  .feature p { font-size: 13px; line-height: 1.5; color: var(--text); }
  .feature-photo { float: left; margin: 3px 12px 4px 0; border-radius: 2px; box-shadow: 0 2px 6px rgba(0,0,0,.2); }

  .feature-architects, .feature-strata { top: 376px; height: 176px; overflow: hidden; }
  .feature-architects p, .feature-strata p { font-size: 12.5px; line-height: 1.45; }
  .feature-architects { left: 22px; width: 380px; }
  .feature-architects .feature-photo { width: 120px; height: 80px; background: linear-gradient(135deg, #5d86b8, #c4d7ea 55%, #7f97a8); }
  .feature-strata { left: 420px; width: 360px; }
  .feature-strata .feature-photo { width: 110px; height: 76px; background: linear-gradient(135deg, #9fb1c9, #e5e7ea 50%, #b06d4c); }

  .feature-specialist { left: 22px; top: 562px; width: 1090px; }
  .feature-specialist h2 { font-size: 20px; }
  .feature-builders { left: 22px; top: 664px; width: 530px; }
  .feature-builders h2 { font-size: 20px; margin-bottom: 4px; }
  .feature-builders p { font-size: 12.5px; line-height: 1.45; }

  .contact-band { position: absolute; left: 570px; top: 656px; width: 570px; height: 104px;
    background: linear-gradient(100deg, var(--blue-deep), var(--blue-dark) 60%, var(--blue)); color: var(--white);
    display: flex; justify-content: space-between; align-items: center; padding: 0 30px; }
  .contact-details { font-size: 22px; line-height: 1.45; }
  .brand { display: flex; align-items: center; gap: 10px; font-size: 17px; font-weight: 700; line-height: 1.2; }
  .brand-mark { width: 14px; height: 14px; background: var(--white); flex: none; }
</style>
</head>
<body>
<main class="flyer">
  <div class="hero-photo" role="img" aria-label="Photo of a modern commercial building at dusk"></div>

  <div class="surveyor-plate">
    <div class="surveyor-name">Dorian Whitcombe</div>
    <div class="surveyor-title">Accredited Building Surveyor</div>
    <div class="surveyor-title">Grade 1 Un Restricted BPB 4812</div>
  </div>

  <article class="card card-quote">
    <div class="card-photo" role="img" aria-label="Photo of surveyors in hi-vis vests on a construction site"></div>
    <div>
      <h3>Get started with a quote today</h3>
      <div class="quote-call">or call</div>
      <div class="quote-phone">(02) 5550 1842</div>
    </div>
  </article>

  <article class="card card-why">
    <div class="card-photo" role="img" aria-label="Photo of a site engineer in a hard hat on the phone"></div>
    <div>
      <h3>Why PCA is your first choice</h3>
      <p>Lorem Ipsum is simply dummy text of the printing and typesetting industry. Lorem Ipsum has been the industry's standard dummy text ever since the 1500s, when an unknown printer took a galley of type and scrambled it to make a type specimen book.</p>
    </div>
  </article>

  <article class="card card-approval">
    <div class="card-photo" role="img" aria-label="Photo of a builder in a hard hat reviewing plans"></div>
    <div>
      <h3>The building approval process explained</h3>
      <p>Lorem Ipsum is simply dummy text of the printing and typesetting industry. Lorem Ipsum has been the industry's standard dummy text ever since the 1500s, when an unknown printer took a galley of type and scrambled it to make a type specimen book.</p>
    </div>
  </article>

  <aside class="specialties">
    <h2>Specialising in</h2>
    <ul>
      <li><svg width="8" height="10" viewBox="0 0 8 10"><path d="M1 1l5 4-5 4" fill="none" stroke="#9a9a9a" stroke-width="2"/></svg>Construction Certificates</li>
      <li><svg width="8" height="10" viewBox="0 0 8 10"><path d="M1 1l5 4-5 4" fill="none" stroke="#9a9a9a" stroke-width="2"/></svg>Complying Development Certificates</li>
      <li><svg width="8" height="10" viewBox="0 0 8 10"><path d="M1 1l5 4-5 4" fill="none" stroke="#9a9a9a" stroke-width="2"/></svg>Performance Based Fire Engineering</li>
      <li><svg width="8" height="10" viewBox="0 0 8 10"><path d="M1 1l5 4-5 4" fill="none" stroke="#9a9a9a" stroke-width="2"/></svg>Building Code of Aust. (BCA) reports</li>
      <li><svg width="8" height="10" viewBox="0 0 8 10"><path d="M1 1l5 4-5 4" fill="none" stroke="#9a9a9a" stroke-width="2"/></svg>Development Feasibility Studies</li>
      <li><svg width="8" height="10" viewBox="0 0 8 10"><path d="M1 1l5 4-5 4" fill="none" stroke="#9a9a9a" stroke-width="2"/></svg>Development Applications</li>
      <li><svg width="8" height="10" viewBox="0 0 8 10"><path d="M1 1l5 4-5 4" fill="none" stroke="#9a9a9a" stroke-width="2"/></svg>Section J Energy Compliance</li>
      <li><svg width="8" height="10" viewBox="0 0 8 10"><path d="M1 1l5 4-5 4" fill="none" stroke="#9a9a9a" stroke-width="2"/></svg>Principal Certifying Authority</li>
      <li><svg width="8" height="10" viewBox="0 0 8 10"><path d="M1 1l5 4-5 4" fill="none" stroke="#9a9a9a" stroke-width="2"/></svg>Building Inspections</li>
      <li><svg width="8" height="10" viewBox="0 0 8 10"><path d="M1 1l5 4-5 4" fill="none" stroke="#9a9a9a" stroke-width="2"/></svg>Strata Fire Safety</li>
    </ul>
  </aside>

  <section class="feature feature-architects">
    <h2>Architects and designers</h2>
    <div class="feature-photo" role="img" aria-label="Photo of a glass office facade against blue sky"></div>
    <p>Expect highly qualified and competent staff with solid backgrounds in construction certification. Plus we have town planners, construction managers, licensed builders, accredited building surveyors and support staff to assist your clients through their building project...</p>
  </section>

  <section class="feature feature-strata">
    <h2>Fire upgrading for strata managers</h2>
    <div class="feature-photo" role="img" aria-label="Photo of an apartment block exterior"></div>
    <p>We deal with Council and owners with relation to Fire Orders, Notices of Intention to Issue orders and Non Compliance works. We speak the council's language. We're able to offer low cost solutions in achieving a safe environment for your occupants...</p>
  </section>

  <section class="feature feature-specialist">
    <h2>Specialist commercial &amp; residential building certifiers</h2>
    <p>Our Company specialises in providing performance based building regulation consultancy. PCA holds the highest level of accreditation in NSW. This level of accreditation means your project is streamlined from concept to completion. Our team provide sound technical advice through accumulated expertise. Through dependable service we nurture trust and have a reputation as a leading Private Certifying Authority in NSW.</p>
  </section>

  <section class="feature feature-builders">
    <h2>We understand builders</h2>
    <p>Our years of on-site building experience means we can offer solutions to challenges you face daily. Our 'can-do-attitude' will help you get things done efficiently and in line with the relevant legislative controls.</p>
  </section>

  <footer class="contact-band">
    <div class="contact-details">
      <div>Kellmere NSW 2099</div>
      <div>f: 02 5550 1843</div>
    </div>
    <div class="brand"><span class="brand-mark"></span><span>Marlowe Fenwick<br>Certifiers</span></div>
  </footer>
</main>
</body>
</html>
```